Back Pain

Need a flyer similar to the attached draft. This is to be handed out to prospective patients. Note that Artwell Studio has already designed the logo. If you need a copy please contact me

```html
<!DOCTYPE html>
<html lang="en">
<head>
<meta charset="utf-8">
<title>Back Pain Relief Clinic Flyer</title>
<link rel="stylesheet" href="https://fonts.googleapis.com/css2?family=Oswald:wght@300;400;500;600;700&family=Montserrat:wght@500;600;700&display=swap">
<style>
  :root {
    --orange: #f96d06;
    --orange-soft: #f8a56b;
    --teal: #0aa0c4;
    --teal-dark: #07809f;
    --ink: #111111;
    --white: #ffffff;
    --panel: #f1f1f2;
    --panel-deep: #e4e4e6;
    --figure-navy: #34486e;
    --figure-plum: #5a2747;
    --figure-rose: #b9506a;
  }
  * { box-sizing: border-box; margin: 0; padding: 0; }
  html, body { width: 960px; height: 1200px; overflow: hidden; }
  body { background: var(--white); font-family: "Oswald", sans-serif; }
  .flyer { position: relative; width: 960px; height: 1200px; background: var(--white); overflow: hidden; }

  .header-shapes { position: absolute; left: 0; top: 0; }
  .clinic-title { position: absolute; left: 70px; top: 58px; color: var(--white); line-height: 1; }
  .clinic-title .line-strong { display: block; font-weight: 600; font-size: 92px; letter-spacing: 1px; }
  .clinic-title .line-light { display: block; font-weight: 400; font-size: 80px; margin-top: 2px; letter-spacing: 0.5px; }
  .brand-name { position: absolute; left: 620px; top: 105px; width: 300px; text-align: center;
    font-family: "Oswald", sans-serif; font-weight: 700; font-size: 58px; line-height: 1.05; color: var(--ink); }

  .info-panel { position: absolute; left: 0; top: 264px; width: 960px; height: 650px;
    background: linear-gradient(135deg, var(--panel-deep) 0%, var(--panel) 35%, var(--white) 75%); }

  .figure-art { position: absolute; left: 150px; top: 289px; width: 160px; height: 596px; border-radius: 70px 70px 20px 20px;
    background: linear-gradient(180deg, var(--figure-plum) 0%, var(--figure-navy) 35%, #2d1c36 70%, var(--figure-rose) 100%); opacity: 0.9; }

  .symptom { position: absolute; height: 37px; border-radius: 0 19px 19px 0;
    background: linear-gradient(90deg, rgba(249,109,6,0) 0%, var(--orange-soft) 35%, var(--orange) 100%);
    color: var(--white); font-weight: 600; font-size: 25px; line-height: 37px; padding-left: 109px; }

  .chart-title { position: absolute; left: 551px; top: 309px; font-size: 21px; line-height: 29px; color: var(--ink); font-weight: 400; }
  .accent { color: var(--orange); font-weight: 600; }
  .strong { font-weight: 600; }
  .tilt-chart { position: absolute; left: 0; top: 0; }
  .axis-label { position: absolute; left: 551px; top: 530px; font-size: 22px; color: var(--ink); }
  .pressure-label { position: absolute; left: 882px; top: 532px; transform: rotate(-90deg); transform-origin: left top;
    font-size: 19px; color: var(--ink); white-space: nowrap; }
  .head-icon { position: absolute; left: 556px; top: 428px; width: 40px; height: 38px; border-radius: 50% 50% 40% 40%;
    background: linear-gradient(180deg, var(--figure-plum), var(--figure-rose)); }

  .usage-pie { position: absolute; left: 492px; top: 588px; }
  .usage-text { position: absolute; left: 624px; top: 594px; width: 284px; text-align: center; color: var(--ink); font-size: 25px; }
  .usage-hours { display: block; margin: 6px 0 6px; height: 45px; line-height: 45px; background: var(--teal); color: var(--white);
    font-weight: 600; font-size: 30px; }

  .care-note { position: absolute; left: 343px; top: 739px; font-size: 28px; line-height: 39.5px; color: var(--ink); }

  .footer-rule { position: absolute; left: 0; top: 914px; width: 960px; height: 8px; background: var(--teal); }
  .footer-panel { position: absolute; left: 0; top: 922px; width: 960px; height: 278px;
    background: linear-gradient(135deg, var(--panel) 0%, var(--white) 40%, var(--white) 100%); }
  .doctor-banner { position: absolute; left: 0; top: 922px; }
  .doctor-name { position: absolute; left: 114px; top: 930px; width: 731px; text-align: center;
    font-family: "Montserrat", sans-serif; font-weight: 700; font-size: 42px; color: var(--white); letter-spacing: 0.5px; }
  .location { position: absolute; left: 0; top: 996px; width: 960px; text-align: center;
    font-family: "Montserrat", sans-serif; font-weight: 600; font-size: 21px; color: var(--ink); }
  .offer { position: absolute; left: 176px; top: 1028px; width: 609px; height: 61px; background: var(--orange);
    border: 1px dashed var(--teal); border-radius: 3px; text-align: center; line-height: 59px;
    color: var(--white); font-weight: 600; font-size: 44px; }
  .booking { position: absolute; left: 0; top: 1100px; width: 960px; text-align: center;
    font-family: "Montserrat", sans-serif; font-weight: 600; font-size: 21px; letter-spacing: 5px; color: var(--ink); }
  .booking .web { color: var(--orange); font-weight: 700; }
  .promo-code { position: absolute; left: 177px; top: 1134px; width: 605px; height: 40px; border: 1.5px dashed var(--teal);
    text-align: center; line-height: 37px; font-family: "Montserrat", sans-serif; font-weight: 600; font-size: 21px;
    letter-spacing: 6px; color: var(--ink); }
  .promo-code .code { color: var(--orange); font-weight: 700; }
</style>
</head>
<body>
<main class="flyer">
  <svg class="header-shapes" width="960" height="264" viewBox="0 0 960 264" aria-hidden="true">
    <polygon points="0,0 469,0 598,264 0,264" fill="var(--orange)"/>
    <polygon points="477,0 524,0 602,264" fill="var(--teal)"/>
  </svg>
  <h1 class="clinic-title"><span class="line-strong">BACK PAIN</span><span class="line-light">RELIEF CLINIC</span></h1>
  <div class="brand-name">POSTURE POINT</div>

  <section class="info-panel" aria-hidden="true"></section>

  <div class="figure-art" role="img" aria-label="Illustration of a man walking while looking down at his phone"></div>

  <div class="symptom" style="left:207px;top:303px;width:262px;">HEADCHES</div>
  <div class="symptom" style="left:207px;top:350px;width:262px;">NECK PAIN</div>
  <div class="symptom" style="left:207px;top:397px;width:298px;">SHOULDER PAIN</div>
  <div class="symptom" style="left:207px;top:445px;width:262px;">BACK PAIN</div>
  <div class="symptom" style="left:207px;top:509px;width:320px;">ARM &amp; HAND PAIN</div>
  <div class="symptom" style="left:207px;top:557px;width:262px;">SCIATICA</div>

  <p class="chart-title">AT THE <span class="accent">HEAD TILTS</span> FORWARD.<br>MORE FORCE IS PLACED ON THE SPINE</p>
  <div class="head-icon" role="img" aria-label="Small illustration of a tilted head"></div>
  <svg class="tilt-chart" width="960" height="540" viewBox="0 0 960 540" aria-label="Pressure on the spine by degree of forward head tilt">
    <g font-family="Oswald, sans-serif" font-weight="600" font-size="22" fill="var(--white)" text-anchor="middle">
      <polygon points="551,492 567,478 567,503 551,503" fill="var(--teal-dark)"/>
      <rect x="567" y="478" width="38" height="25" fill="var(--teal)"/>
      <text x="586" y="499">12</text>
      <polygon points="614,462 630,448 630,503 614,503" fill="var(--teal-dark)"/>
      <rect x="630" y="448" width="38" height="55" fill="var(--teal)"/>
      <text x="649" y="475">27</text>
      <polygon points="677,437 693,423 693,503 677,503" fill="var(--teal-dark)"/>
      <rect x="693" y="423" width="37" height="80" fill="var(--teal)"/>
      <text x="712" y="451">40</text>
      <polygon points="740,417 756,403 756,503 740,503" fill="var(--teal-dark)"/>
      <rect x="756" y="403" width="37" height="100" fill="var(--teal)"/>
      <text x="775" y="431">49</text>
      <polygon points="802,390 818,376 818,503 802,503" fill="var(--teal-dark)"/>
      <rect x="818" y="376" width="38" height="127" fill="var(--teal)"/>
      <text x="837" y="404">60</text>
    </g>
    <g font-family="Montserrat, sans-serif" font-weight="500" font-size="13" fill="var(--ink)" text-anchor="middle">
      <text x="578" y="525">0°</text>
      <text x="641" y="525">15°</text>
      <text x="704" y="525">30°</text>
      <text x="767" y="525">45°</text>
      <text x="829" y="525">60°</text>
    </g>
  </svg>
  <p class="axis-label">DEGREES OF <span class="strong">FORWARD HEAD TILT</span></p>
  <p class="pressure-label">PRESSURE ON SPINR (LBS)</p>

  <svg class="usage-pie" width="122" height="122" viewBox="0 0 122 122" aria-label="Pie chart of daily device use">
    <circle cx="61" cy="61" r="60" fill="var(--panel-deep)"/>
    <circle cx="61" cy="61" r="54" fill="var(--orange)"/>
    <path d="M61,61 L61,7 A54,54 0 0 1 88,108 Z" fill="var(--teal)"/>
  </svg>
  <p class="usage-text">THE AVERAGE PERSON SPENDS
    <span class="usage-hours">8-10 HOURS PER DAY</span>
    USING <span class="accent">ELECTRONIC DEVICES</span></p>

  <p class="care-note"><span class="accent">CHIROPRACTIC CARE CAN HELP</span> CORRECT<br>
    AND PREVENT THESE PROBLEMS BY <span class="accent">RESTORING</span><br>
    AND <span class="accent">MAINTAINING</span><br>
    <span class="accent">PROPER ALIGNMENT</span> OF THE <span class="accent">NECK</span></p>

  <div class="footer-rule"></div>
  <section class="footer-panel" aria-hidden="true"></section>
  <svg class="doctor-banner" width="960" height="62" viewBox="0 0 960 62" aria-hidden="true">
    <polygon points="114,0 845,0 819,62 140,62" fill="var(--teal)"/>
  </svg>
  <h2 class="doctor-name">DR. HELEN MARSH</h2>
  <p class="location">NOW IN KELSEY BAY AT : 42 HARBOUR RD.</p>
  <p class="offer">50% OFF INITIAL CONSULTATION</p>
  <p class="booking">IF YOU BOOK ONLINE AT <span class="web">WWW.POSTUREPOINT.COM.AU</span></p>
  <p class="promo-code">USE CODE <span class="code">"POSTURE POINT"</span> OPTION</p>
</main>
</body>
</html>
```